Nine Quills Ink, "Writing and Editing Done Write"

We need a brochure that provides background about our company, identifies our products and services and provides our contact information. If possible, We would like the designer to use an Office suite product such as Word or Publisher to create the brochure if possible. We would like photos, color, something that inspires customers to use our services. We have attached a copy of a draft brochure and we believe the text in the brochure is good, but the brochure is cold, bland and lacks color, style and a fresh quality. We would like all text in the brochure to be included as well as the attached logo and company name somewhere on the front and back of the brochure. Please feel free to resize the logo and use creative license to develop the brochure as you please. However, the brochure colors should compliment the dark blue, light blue and black colors in the logo. Most of all, the brochure needs to be engaging, inviting, fresh and ultra professional. Thanks!

Target Market(s)

Small and large scale businesses who would use self-help books, writing services for blogs and Chatterloop posts, newsletters and manuscript reviews.

Industry/Entity Type

Marketing

Font styles to use
Serif

Colors
0655a3
3377b5
85acd3
000000

Requirements
Must have
• -Logo and company name; text in draft brochure
• -Color and business photos which relate to the products/services provided
• -Inspiring, engaging, professional feel and style
• -I would like colors which compliment the logo colors (perhaps the colors below, but we are open to designer choices
• -Since this is a writing/editing business, something in the brochure that reflects that would be good.
Nice to have
• -Open; depends on the designer preference
• -Use of Office Word or Publisher program, but we are open to the use of other programs.
Should not have
• -Bland brochure with only text

```html
<!DOCTYPE html>
<html lang="en">
<head>
<meta charset="utf-8">
<title>Nine Quills Ink – Trifold Brochure</title>
<link href="https://fonts.googleapis.com/css2?family=Montserrat:wght@500;800&family=Roboto+Condensed:wght@300;700&family=Noto+Serif&family=Dancing+Script:wght@500&display=swap" rel="stylesheet">
<style>
  :root {
    --navy: #2c2f8e;
    --navy-deep: #1f2578;
    --periwinkle: #a6a9db;
    --periwinkle-soft: #d7d8ef;
    --paper: #f1f1f3;
    --paper-edge: #e4e4e8;
    --ink: #1b1b1f;
    --body-grey: #4a4a52;
    --hatch-grey: #6e6f76;
    --scene: #d9d9dc;
  }
  * { margin: 0; padding: 0; box-sizing: border-box; }
  html, body { width: 837px; height: 1200px; overflow: hidden; background: var(--scene); }
  .canvas { position: relative; width: 837px; height: 1200px; }

  .brochure { position: absolute; left: 20px; top: 290px; width: 797px; height: 603px;
    box-shadow: 0 6px 18px rgba(0,0,0,.18); }
  .base-strip { position: absolute; left: 20px; top: 893px; width: 797px; height: 12px; background: var(--ink); }
  .base-strip .tab { position: absolute; top: -6px; width: 70px; height: 6px; background: var(--navy); }

  .panel { position: absolute; top: 0; height: 603px; overflow: hidden; }
  .panel--services { left: 0; width: 261px; background: linear-gradient(180deg, var(--paper), var(--paper-edge)); }
  .panel--contact { left: 261px; width: 262px; background: linear-gradient(180deg, var(--navy) 0%, var(--navy-deep) 100%); }
  .panel--cover { left: 523px; width: 274px; background: var(--paper); }

  /* services panel */
  .icon-badge { position: absolute; left: 50%; width: 78px; height: 78px; margin-left: -39px; border-radius: 50%;
    background: var(--periwinkle-soft); display: flex; align-items: center; justify-content: center; }
  .icon-badge__inner { width: 62px; height: 62px; border-radius: 50%; background: #fff; display: flex; align-items: center; justify-content: center; }
  .pill-heading { position: absolute; left: 50%; transform: translateX(-50%); height: 36px; border-radius: 18px;
    background: var(--navy); color: #fff; font-family: "Roboto Condensed", sans-serif; font-weight: 700;
    font-size: 21px; line-height: 36px; text-align: center; white-space: nowrap; padding: 0 18px; }
  .body-copy { position: absolute; left: 18px; width: 225px; font-family: "Roboto Condensed", sans-serif; font-weight: 300;
    font-size: 10.2px; line-height: 15.6px; color: var(--body-grey); text-align: center; }

  /* contact panel */
  .photo { position: absolute; border-radius: 50%; border: 5px solid #fff; }
  .photo--writer { left: 15px; top: 8px; width: 184px; height: 184px; background: linear-gradient(135deg, #6b5a4a, #c9b9a6 60%, #e8e4e0); }
  .photo--idea { left: 164px; top: 136px; width: 94px; height: 94px; background: radial-gradient(circle at 45% 40%, #cfd3d8, #6f747b); }
  .wordmark { position: absolute; display: flex; align-items: center; gap: 8px; font-family: "Montserrat", sans-serif; font-weight: 500; white-space: nowrap; }
  .wordmark__square { display: inline-block; }
  .wordmark--contact { left: 32px; top: 286px; color: #fff; font-size: 17px; }
  .wordmark--contact .wordmark__square { width: 14px; height: 14px; background: #fff; }
  .world-map { position: absolute; left: 12px; top: 370px; width: 238px; height: 74px; border-radius: 40px;
    background: radial-gradient(ellipse at center, rgba(90,110,210,.55), rgba(44,47,142,0) 70%); }
  .pill-touch { position: absolute; left: 50%; top: 398px; transform: translateX(-50%); height: 26px; border-radius: 13px; padding: 0 18px;
    background: var(--periwinkle); color: var(--navy-deep); font-family: "Noto Serif", serif; font-size: 16px; line-height: 26px; white-space: nowrap; }
  .contact-icons { position: absolute; left: 50%; top: 428px; transform: translateX(-50%); display: flex; gap: 3px; }
  .contact-icons span { width: 12px; height: 12px; border-radius: 50%; background: #fff; display: flex; align-items: center; justify-content: center; }
  .contact-lines { position: absolute; left: 0; top: 448px; width: 262px; text-align: center; font-family: "Montserrat", sans-serif;
    font-size: 11px; line-height: 16.2px; color: #fff; font-style: normal; }
  .web-icon { position: absolute; left: 50%; margin-left: -17px; width: 34px; height: 34px; border-radius: 50%; display: flex; align-items: center; justify-content: center; }
  .panel--contact .web-icon { top: 549px; border: 2px solid rgba(255,255,255,.6); }
  .web-url { position: absolute; left: 0; width: 100%; top: 584px; text-align: center; font-family: "Montserrat", sans-serif; font-size: 11.5px; letter-spacing: .4px; }
  .panel--contact .web-url { color: #fff; }
  .web-url b { font-weight: 800; }

  /* cover panel */
  .wordmark--cover { left: 40px; top: 64px; color: var(--ink); font-size: 18px; }
  .wordmark--cover .wordmark__square { width: 16px; height: 16px; background: var(--navy); }
  .cover-photo { position: absolute; left: 0; top: 140px; width: 274px; height: 400px;
    background: linear-gradient(160deg, #3c40a0 0%, #5c61b8 40%, #2c2f8e 100%); }
  .cover-accent { position: absolute; left: 0; top: 245px; width: 4px; height: 135px; background: rgba(255,255,255,.35); }
  .cover-title { position: absolute; left: 34px; top: 368px; font-family: "Montserrat", sans-serif; font-weight: 800; font-size: 35px; line-height: 38px; color: #fff; }
  .cover-tagline { position: absolute; left: 34px; top: 453px; font-family: "Dancing Script", cursive; font-size: 17.5px; color: #fff; white-space: nowrap; }
  .cover-band { position: absolute; left: 95px; top: 503px; width: 190px; height: 28px; background: var(--hatch-grey); transform: skewX(-38deg); }
  .cover-bottom { position: absolute; left: 0; top: 528px; width: 274px; height: 75px; background: var(--paper); }
  .panel--cover .web-icon { top: 549px; border: 2px solid var(--periwinkle); background: #fff; }
  .panel--cover .web-url { color: var(--ink); }
</style>
</head>
<body>
<div class="canvas">
  <article class="brochure">

    <section class="panel panel--services">
      <div class="icon-badge" style="top:21px">
        <div class="icon-badge__inner">
          <svg width="34" height="30" viewBox="0 0 34 30" fill="none" stroke="#1b1b1f" stroke-width="1.6">
            <rect x="9" y="2" width="16" height="16"/><line x1="12" y1="7" x2="22" y2="7"/><line x1="12" y1="11" x2="22" y2="11"/>
            <path d="M2 12 L2 28 L32 28 L32 12 L17 22 Z"/>
          </svg>
        </div>
      </div>
      <h2 class="pill-heading" style="top:109px;width:166px">Newsletters</h2>
      <p class="body-copy" style="top:156px">Email newsletters allow you to keep current and prospective customers informed about your brand and engaged with your product and service offerings. Newsletters represent an ideal path to identify target audiences and maintain open lines of communication to encourage prospective sales/services.</p>

      <div class="icon-badge" style="top:286px">
        <div class="icon-badge__inner">
          <svg width="34" height="32" viewBox="0 0 34 32" fill="none" stroke="#1b1b1f" stroke-width="1.6">
            <path d="M6 12 H11 V24 H6 Z"/><path d="M11 13 L16 5 Q19 4 18 9 L17 12 H25 Q27 13 26 15 L24 22 Q23 24 21 24 H11"/>
            <path d="M7 28 l1.5 2 l-2.3 -.8 h2.8 l-2.3 .8 Z M16 28 l1.5 2 l-2.3 -.8 h2.8 l-2.3 .8 Z M25 28 l1.5 2 l-2.3 -.8 h2.8 l-2.3 .8 Z"/>
          </svg>
        </div>
      </div>
      <h2 class="pill-heading" style="top:375px;width:214px">Manuscript Reviews</h2>
      <p class="body-copy" style="top:421px">As published writers, we understand the value of reviews and we see reviews as a collaborative process that allows manuscripts to be evaluated and commented upon by experts within the same field of research. The evaluation and critique generated from the review provides authors with feedback to improve their work and allows editors to assess the manuscript suitability for publication.</p>
      <p class="body-copy" style="top:547px">Contact us for a free consultation with one of our seasoned staff of writers and/or editors to help guide you along the path to success!</p>
    </section>

    <section class="panel panel--contact">
      <div class="photo photo--writer" role="img" aria-label="Photo of a smiling writer holding an open book in a library"></div>
      <div class="photo photo--idea" role="img" aria-label="Photo of a light bulb resting on a chalkboard sketch"></div>
      <div class="wordmark wordmark--contact"><span class="wordmark__square"></span>Nine Quills Ink</div>
      <div class="world-map" role="img" aria-label="Faint world map behind the contact details"></div>
      <h3 class="pill-touch">Get In Touch</h3>
      <div class="contact-icons" aria-hidden="true">
        <span><svg width="7" height="8" viewBox="0 0 7 8"><path d="M3.5 8 L1 4 A2.6 2.6 0 1 1 6 4 Z" fill="#2c2f8e"/></svg></span>
        <span><svg width="7" height="7" viewBox="0 0 7 7"><path d="M1 1 L2.6 .8 L3 2.5 L2.2 3 Q3 4.5 4.2 4.8 L4.6 4 L6.2 4.5 L6 6 Q2 6 1 1 Z" fill="#2c2f8e"/></svg></span>
        <span><svg width="7" height="6" viewBox="0 0 7 6"><rect x=".5" y=".8" width="6" height="4.4" fill="none" stroke="#2c2f8e"/><path d="M.5 .8 L3.5 3.2 L6.5 .8" fill="none" stroke="#2c2f8e"/></svg></span>
      </div>
      <address class="contact-lines">480 Larkspur Lane, Suite 212<br>Fairhaven, OR 97455<br>541/555-0187<br>hello@ninequillsink.com</address>
      <div class="web-icon">
        <svg width="18" height="18" viewBox="0 0 18 18" fill="none" stroke="#fff" stroke-width="1.2"><circle cx="9" cy="9" r="7.5"/><ellipse cx="9" cy="9" rx="3.5" ry="7.5"/><line x1="1.5" y1="9" x2="16.5" y2="9"/></svg>
      </div>
      <p class="web-url">www.<b>ninequillsink</b>.com</p>
    </section>

    <section class="panel panel--cover">
      <div class="wordmark wordmark--cover"><span class="wordmark__square"></span>Nine Quills Ink</div>
      <div class="cover-photo" role="img" aria-label="Blue-toned photo of a writer in glasses reading a tablet"></div>
      <div class="cover-accent"></div>
      <h1 class="cover-title">NINE<br>QUILLS INK</h1>
      <p class="cover-tagline">"Writing and editing done right"</p>
      <div class="cover-band"></div>
      <div class="cover-bottom"></div>
      <div class="web-icon">
        <svg width="18" height="18" viewBox="0 0 18 18" fill="none" stroke="#2c2f8e" stroke-width="1.2"><circle cx="9" cy="9" r="7.5"/><ellipse cx="9" cy="9" rx="3.5" ry="7.5"/><line x1="1.5" y1="9" x2="16.5" y2="9"/></svg>
      </div>
      <p class="web-url">www.<b>ninequillsink</b>.com</p>
    </section>

  </article>
  <div class="base-strip">
    <span class="tab" style="left:0"></span>
    <span class="tab" style="left:262px;width:40px"></span>
    <span class="tab" style="right:0"></span>
  </div>
</div>
</body>
</html>
```